Corridor Works

Small ageny public transit advocacy, funding and compliance.
Consulting and lobbying efforts for small public transit agencies and communities exploring public transit opportunities.

I was interested in a simple line sketch suggesting motion, mobility. The card will be black on white. I would like it to include the bUs ones brief; Advocacy, Funding , and Compliance for small transit agencies.

Reason: I have been traveling and have had limited time to respond. Thank you all for your submit talks.

Industry/Entity Type

Consulting

Contact Information for Business Card

Paul R Vesby
Phone (907) 418-2960
Email paulrvesby@mailnook.net

```html
<!DOCTYPE html>
<html lang="en">
<head>
<meta charset="utf-8">
<title>Corridor Works – Business Card</title>
<link rel="stylesheet" href="https://fonts.googleapis.com/css2?family=Open+Sans:wght@600;700&display=swap">
<style>
  :root {
    --page-bg: #151515;
    --metal-light: #e6e8ea;
    --metal-mid: #b9bcbf;
    --metal-dark: #8e9195;
    --metal-shine: #ffffff;
    --stripe-white: #f7f7f7;
    --plate-dark: #2a2a2a;
    --plate-mid: #3c3c3c;
    --text-light: #ffffff;
  }
  * { margin: 0; padding: 0; box-sizing: border-box; }
  html, body {
    width: 1200px;
    height: 675px;
    overflow: hidden;
    background: var(--page-bg);
  }
  .business-card {
    position: absolute;
    left: 141px;
    top: 79px;
    width: 917px;
    height: 517px;
    font-family: "Open Sans", "Helvetica Neue", Arial, sans-serif;
    color: var(--text-light);
    overflow: hidden;
  }
  .metal-band {
    position: absolute;
    left: 0;
    width: 100%;
    background:
      radial-gradient(ellipse 30% 90% at 62% 50%, rgba(255,255,255,0.85), rgba(255,255,255,0) 70%),
      linear-gradient(90deg, var(--metal-dark) 0%, var(--metal-mid) 25%, var(--metal-light) 55%, var(--metal-mid) 80%, var(--metal-dark) 100%);
  }
  .metal-band--top { top: 0; height: 70px; }
  .metal-band--bottom { bottom: 0; height: 63px; }
  .white-stripe {
    position: absolute;
    left: 0;
    width: 100%;
    background: var(--stripe-white);
  }
  .white-stripe--top { top: 70px; height: 24px; }
  .white-stripe--bottom { top: 432px; height: 22px; }
  .dark-plate {
    position: absolute;
    left: 0;
    top: 94px;
    width: 100%;
    height: 338px;
    background:
      radial-gradient(ellipse 60% 80% at 50% 40%, var(--plate-mid), rgba(60,60,60,0) 80%),
      linear-gradient(180deg, var(--plate-mid) 0%, var(--plate-dark) 100%);
  }
  .tagline {
    position: absolute;
    top: 132px;
    left: 0;
    width: 100%;
    text-align: center;
    font-size: 24px;
    font-weight: 600;
    line-height: 1;
    white-space: nowrap;
  }
  .company-name {
    position: absolute;
    left: 58px;
    top: 253px;
    font-size: 58px;
    font-weight: 600;
    line-height: 1;
    white-space: nowrap;
  }
  .contact {
    position: absolute;
    right: 58px;
    text-align: right;
    line-height: 1;
    white-space: nowrap;
  }
  .contact__name { top: 239px; font-size: 38px; font-weight: 600; }
  .contact__phone { top: 341px; font-size: 26px; font-weight: 600; }
  .contact__email { top: 374px; font-size: 26px; font-weight: 600; }
</style>
</head>
<body>
  <main class="business-card">
    <div class="metal-band metal-band--top"></div>
    <div class="white-stripe white-stripe--top"></div>
    <div class="dark-plate"></div>
    <div class="white-stripe white-stripe--bottom"></div>
    <div class="metal-band metal-band--bottom"></div>

    <p class="tagline">“ Advocacy, Funding , and Compliance for small transit agencies ”</p>
    <h1 class="company-name">Corridor Works</h1>
    <p class="contact contact__name">Paul R Vesby</p>
    <p class="contact contact__phone">(907) 418-2960</p>
    <p class="contact contact__email">paulrvesby@mailnook.net</p>
  </main>
</body>
</html>
```